Book Cover for Memoir: Sexual Assault and Traumatic Stress

I need a cover design for a memoir that is a victim's story of a sexual assault. I will need a print-on-demand cover, an eBook cover, and a 3D thumbnail image. The thumbnail and eBook cover will be used immediately, and the POD cover will be used in a few months with the full manuscript is ready. Therefore, I need an artist who is willing to make small adjustments if needed once the page count is set.

I have a image I have purchased that should give you an idea of the desired direction, but you can feel free to use your own images. I have attached some examples of book covers I like. I attached a color palette for fonts.

Overall Look: Fonts should be feminine and thin, but large to stand out. Look should be simple and elegant, and display and overall depressing feeling. There should be enough detail though to make it look professionally put together. Not TOO minimalistic.

I have also attached the Print Harbor templates if you choose to use those. If not, ensure there is an open place for the barcode on the bottom right.

Requirements
Must have
• Title: Beneath Quiet Rain
Subtitle: One Woman's Account of Fear, Guilt & Silence
Author: Dana Ruth Whitford
Audience: Mostly women 18-30
Quote (for the back): "I always thought I'd know how I'd react if I ever was raped. I was wrong. I've been wrong a lot lately."
Summary (back cover): When twenty-seven-year-old Dana Whitford wakes up with a gut-wrenching feeling, she has little memory of the horrifying events that occurred the night before. Days earlier, Dana was a spirited single mom who had abandoned her hometown to raise her daughter in the city and pursue her dreams. In the short months since Dana’s move to Seattle, she became the adored lover of a charismatic lawyer, started a new business, and finally felt life was going her way. So what happened to cause her to break?

In a gripping and heartbreaking narrative, Dana tells the true story of how her life unraveled from the traumatic events that took place that night and why what seems obvious to everyone else is impossible for Dana to believe. Beneath Quiet Rain is a chilling exploration of memory through trauma, trust in humanity, and a captivating story of strength and survival that appeals to the heart of fathers and mothers, sons and daughters, and men and women alike.
Nice to have
• BACK COVER: I'd like to have a photo on the back. This should depict the happy life of the main character before the sexual assault, and should be with her daughter. Or should be a nature scene that starts at the corner and blends into the rest of the cover. I have attached a possible image or you can use something you like.

```html
<!DOCTYPE html>
<html lang="en">
<head>
<meta charset="utf-8">
<title>Beneath Quiet Rain — Spine and Front Cover</title>
<link rel="stylesheet" href="https://fonts.googleapis.com/css2?family=Antonio:wght@200;300&family=Oswald:wght@300;400&family=Poiret+One&display=swap">
<style>
  :root {
    --page-bg: #ffffff;
    --title-teal: #2bb0b1;
    --title-shade: rgba(20, 70, 75, 0.35);
    --author-ink: #3b3838;
    --subtitle-ink: #f4f1ee;
    --spine-navy: #3e4872;
    --spine-navy-dark: #333c62;
    --spine-white: #f2f2f4;
    --skin-light: #eedad2;
    --fabric-rose: #dcc3bb;
    --water-mist: #a9b1aa;
    --water-deep: #5d6c74;
    --hair-dark: #2e3442;
  }
  html, body {
    margin: 0;
    padding: 0;
    width: 869px;
    height: 1200px;
    overflow: hidden;
    background: var(--page-bg);
  }
  .book {
    position: absolute;
    top: 25px;
    left: 6px;
    width: 857px;
    height: 1150px;
    display: flex;
  }

  /* Spine */
  .spine {
    position: relative;
    width: 90px;
    height: 100%;
    background: linear-gradient(90deg, var(--spine-navy-dark) 0%, var(--spine-navy) 60%, var(--spine-navy-dark) 100%);
    overflow: hidden;
  }
  .spine-text {
    position: absolute;
    top: 0;
    left: 90px;
    width: 1150px;
    height: 90px;
    transform-origin: 0 0;
    transform: rotate(90deg);
    display: flex;
    align-items: center;
    padding: 0 40px;
    box-sizing: border-box;
  }
  .spine-title {
    font-family: "Antonio", sans-serif;
    font-weight: 200;
    font-size: 66px;
    line-height: 1;
    color: var(--title-teal);
    white-space: nowrap;
    letter-spacing: 1px;
  }
  .spine-subtitle {
    margin-left: 22px;
    font-family: "Oswald", sans-serif;
    color: var(--spine-white);
    line-height: 1.1;
    white-space: nowrap;
  }
  .spine-subtitle-lead { display: block; font-weight: 300; font-size: 22px; }
  .spine-subtitle-themes { display: block; font-weight: 400; font-size: 27px; }
  .spine-author {
    margin-left: auto;
    font-family: "Poiret One", sans-serif;
    font-size: 36px;
    color: var(--title-teal);
    white-space: nowrap;
  }

  /* Front cover */
  .front {
    position: relative;
    width: 767px;
    height: 100%;
    overflow: hidden;
  }
  .cover-photo {
    position: absolute;
    inset: 0;
    background:
      radial-gradient(ellipse 55% 30% at 45% 88%, var(--hair-dark) 0%, rgba(46,52,66,0) 70%),
      radial-gradient(ellipse 60% 35% at 30% 25%, rgba(255,255,255,0.55) 0%, rgba(255,255,255,0) 70%),
      linear-gradient(180deg, var(--skin-light) 0%, var(--fabric-rose) 30%, #c8bcb2 50%, var(--water-mist) 68%, var(--water-deep) 100%);
  }
  .author {
    position: absolute;
    top: 100px;
    left: 0;
    right: 0;
    margin: 0;
    text-align: center;
    font-family: "Poiret One", sans-serif;
    font-size: 40px;
    color: var(--author-ink);
  }
  .title { margin: 0; }
  .title-word {
    position: absolute;
    font-family: "Antonio", sans-serif;
    font-weight: 200;
    font-size: 130px;
    line-height: 1;
    color: var(--title-teal);
    text-shadow: 3px 4px 4px var(--title-shade);
    letter-spacing: -1px;
  }
  .title-word--first { top: 225px; left: 38px; }
  .title-word--second { top: 345px; left: 350px; }
  .title-word--third { top: 465px; left: 545px; }
  .subtitle {
    position: absolute;
    top: 515px;
    right: 235px;
    margin: 0;
    text-align: right;
    font-family: "Oswald", sans-serif;
    color: var(--subtitle-ink);
    text-shadow: 1px 2px 3px rgba(40, 40, 40, 0.45);
    line-height: 1.15;
  }
  .subtitle-lead { display: block; font-weight: 300; font-size: 24px; }
  .subtitle-themes { display: block; font-weight: 400; font-size: 30px; }
</style>
</head>
<body>
  <div class="book">
    <aside class="spine">
      <div class="spine-text">
        <span class="spine-title">BENEATH QUIET RAIN</span>
        <span class="spine-subtitle">
          <span class="spine-subtitle-lead">One Woman's Account of</span>
          <span class="spine-subtitle-themes">Fear, Guilt &amp; Silence</span>
        </span>
        <span class="spine-author">Dana Ruth Whitford</span>
      </div>
    </aside>
    <main class="front">
      <div class="cover-photo" role="img" aria-label="Photograph of a dark-haired young woman lying in pale water in a white dress, seen from above"></div>
      <p class="author">Dana Ruth Whitford</p>
      <h1 class="title" aria-label="Beneath Quiet Rain">
        <span class="title-word title-word--first">BENEATH</span>
        <span class="title-word title-word--second">QUIET</span>
        <span class="title-word title-word--third">RAIN</span>
      </h1>
      <p class="subtitle">
        <span class="subtitle-lead">One Woman's Account of</span>
        <span class="subtitle-themes">Fear, Guilt &amp; Silence</span>
      </p>
    </main>
  </div>
</body>
</html>
```